MO&A - Business Card and Stationery for a Law Firm
Mendívil Ortuzar & Asociados
Professional
Julián Esteban Mendívil Ortuzar
Abogado
Carrera 48 No. 62-14 Of. 305
Bogotá D.C., Colombia
julian.mendivil@mendivilortuzar.com
www.mendivilortuzar.com
The text on the back of the card is in Spanish, for your information the meaning in English is as follows:
Companies in Colombia and abroad.
International business.
Tax planning.
Foreign investments.
Inmigration.
Industrial property.
Please distribute the text as you consider.
Logo and the following text:
Sociedades en Colombia y el exterior.
Negocios internacionales.
Planeación tributaria.
Inversión extranjera.
Asuntos migratorios.
Propiedad Industrial.

```html
<!DOCTYPE html>
<html lang="es">
<head>
<meta charset="utf-8">
<title>Mendívil Ortuzar &amp; Asociados – Tarjeta</title>
<link href="https://fonts.googleapis.com/css2?family=Cinzel:wght@400&family=Tinos&display=swap" rel="stylesheet">
<style>
  :root {
    --navy: #1b2b4d;
    --ink: #1f2430;
    --grey-text: #8a8d93;
    --divider: #b9bcc2;
    --swoosh: #a9adb4;
    --card: #ffffff;
    --backdrop: #ecebe8;
  }
  * { margin: 0; padding: 0; box-sizing: border-box; }
  html, body { width: 1200px; height: 778px; overflow: hidden; }
  body { background: var(--backdrop); position: relative; font-family: "Tinos", "Times New Roman", serif; color: var(--ink); }
  .business-card {
    position: absolute; left: 168px; top: 137px; width: 864px; height: 504px;
    background: var(--card); overflow: hidden;
    box-shadow: 0 6px 18px rgba(0,0,0,.18);
  }
  .firm-mark { position: absolute; left: 150px; top: 74px; display: flex; align-items: center; gap: 24px; }
  .firm-mark__square { width: 88px; height: 88px; background: var(--navy); }
  .firm-mark__name {
    font-family: "Cinzel", "Times New Roman", serif; font-weight: 400; color: var(--navy);
    font-size: 38px; line-height: 44px; letter-spacing: 1px;
  }
  .divider { position: absolute; left: 444px; top: 212px; width: 1px; height: 172px; background: var(--divider); }
  .holder { position: absolute; right: calc(864px - 424px); top: 272px; text-align: right; }
  .holder__name { font-family: "Cinzel", "Times New Roman", serif; font-size: 22px; color: var(--ink); letter-spacing: .5px; white-space: nowrap; }
  .holder__role { font-size: 17px; color: var(--grey-text); margin-top: 0; }
  .contact { position: absolute; left: 474px; top: 216px; list-style: none; font-size: 20px; line-height: 32px; }
  .contact li { display: flex; align-items: center; white-space: nowrap; }
  .contact .icon { width: 18px; height: 18px; margin-right: 12px; fill: none; stroke: var(--ink); stroke-width: 1.6; }
  .contact .email { font-size: 19px; }
  .card-band { position: absolute; left: 0; bottom: 0; width: 864px; height: 150px; }
  .website {
    position: absolute; left: 0; right: 0; bottom: 30px; text-align: center;
    color: #fff; font-size: 22px; letter-spacing: 4px;
  }
</style>
</head>
<body>
  <article class="business-card">
    <div class="firm-mark">
      <div class="firm-mark__square"></div>
      <div class="firm-mark__name">Mendívil Ortuzar<br>&amp; Asociados</div>
    </div>

    <div class="holder">
      <p class="holder__name">Julián Esteban Mendívil Ortuzar</p>
      <p class="holder__role">Abogado</p>
    </div>

    <div class="divider"></div>

    <ul class="contact">
      <li>Carrera 48 No. 62-14 Of. 305</li>
      <li>Bogotá D.C., Colombia</li>
      <li><svg class="icon" viewBox="0 0 18 18"><path d="M4 2 L7 5 L5.5 7 Q7.5 11 11 12.5 L13 11 L16 14 L14 16 Q6 15 2 4 Z"/></svg>+57 (1) 5304729</li>
      <li><svg class="icon" viewBox="0 0 18 18"><rect x="5" y="1.5" width="8" height="15" rx="1.5"/><line x1="8" y1="14" x2="10" y2="14"/></svg>+57 3157420963</li>
      <li class="email"><svg class="icon" viewBox="0 0 18 18"><rect x="1.5" y="4" width="15" height="10"/><path d="M1.5 4 L9 10 L16.5 4"/></svg>julian.mendivil@mendivilortuzar.com</li>
    </ul>

    <svg class="card-band" viewBox="0 0 864 150" preserveAspectRatio="none" aria-hidden="true">
      <path d="M0 62 Q432 -8 864 62 L864 74 Q432 10 0 74 Z" fill="var(--swoosh)"/>
      <path d="M0 74 Q432 10 864 74 L864 150 L0 150 Z" fill="var(--navy)"/>
    </svg>
    <p class="website">www.mendivilortuzar.com</p>
  </article>
</body>
</html>
```